Real Estate | Property Management Website Design

We are working with a Real Estate company in California. They provide Property Management Services and Real Estate Services.

PLEASE NOT: make sure the site covers real estate and property management).

A few websites for inspiration:
https://pinebrookleases.com
https://www.varmolhomeadvisors.com
https://marisotelvy.com
https://tobenhalvrick.com
https://thecalvenparty.com
https://ronaquistmoor.com
https://zvask.com

Thank you for taking the time to consider designing a website for us. We are web developers based in Stockton, CA, USA. Most of our projects go through the same process. Understanding this process may help you win a project with us. We custom-code all of our websites in-house. We don’t have any requirements as to what tools you use for your design, but we ask that you follow these guidelines.

IMAGES:
If you use any images or icons in the design, we ask that you have a link to the asset so we can purchase the image/icon. Most of the designs we submit do not have the customer’s images on them unless they have some great images. Be creative; show us the feeling you are trying to portray with your image choices. Use any royalty-free site you choose. We subscribe to Plimora and mainly use their images, but we can purchase images outside of Plimora. PLEASE NOTE: we will not submit designs to clients with watermarks on the images.

FONTS:
We ask that you identify the fonts you’re using in the design. This can be done in a message if you want. We typically use Quendle Fonts and Plimora Fonts.

CONTENT:
We're always open to different content and ideas. We often submit designs with stock images so the client can see our vision. We typically take pictures after the website launch to use their images with our vision. Lorem Ipsum is fine for paragraphs, but we ask that you make the Headers with correct English. We want to be able to show the vision and identify the sections of the website.

INSPIRATION:
We typically add a couple of links in the brief of websites we like to help you get started in your design.

REVISIONS:
We do not often ask for revisions of the designs unless we see something in the design that may not appeal to the client. If there are slight changes that we want to make, we do that in the development process.

FEEDBACK:
We rarely give feedback on designs during the design process. We are working on many website projects and do not have the time to provide feedback. We usually respond if your request is well thought out and asks specific questions, but a note asking “feedback, please” usually goes unanswered.

```html
<!DOCTYPE html>
<html lang="en">
<head>
<meta charset="utf-8">
<title>Crestvale Properties</title>
<link href="https://fonts.googleapis.com/css2?family=Poppins:wght@300;400;500;600;700&family=Dancing+Script:wght@600&display=swap" rel="stylesheet">
<style>
:root{
  --orange:#ff8532;
  --ink:#333333;
  --text:#555555;
  --white:#ffffff;
  --light:#f3f3f3;
  --line:#e2e2e2;
}
*{margin:0;padding:0;box-sizing:border-box}
html,body{width:1200px;height:4898px;overflow:hidden;background:var(--white);font-family:'Poppins',sans-serif;color:var(--ink)}
.page{position:relative;width:1200px;height:4898px}
.abs{position:absolute}
.photo{position:absolute}
.btn-outline{position:absolute;border:1.5px solid var(--orange);color:var(--orange);font-size:16px;display:flex;align-items:center;justify-content:center;background:var(--white)}
.para{position:absolute;font-size:14.5px;line-height:29.6px;color:var(--text)}

/* hero */
.hero{left:0;top:0;width:1200px;height:737px;background:linear-gradient(180deg,#6f7680 0%,#9a8f84 30%,#7a6a5a 55%,#3f6a6c 75%,#4a4036 100%)}
.hero-shade{left:0;top:0;width:1200px;height:737px;background:linear-gradient(180deg,rgba(0,0,0,.35),rgba(0,0,0,.1) 40%,rgba(0,0,0,.25))}
.topbar{left:0;top:0;width:1200px;height:120px;border-bottom:1px solid rgba(255,255,255,.3)}
.nav{top:50px;left:74px;display:flex;align-items:center;gap:28px;color:var(--white);font-size:14px;font-weight:600;letter-spacing:.3px}
.burger{width:22px;height:16px;display:flex;flex-direction:column;justify-content:space-between}
.burger span{height:3px;background:var(--white);display:block}
.brand{display:flex;align-items:center;gap:10px}
.brand-mark{width:18px;height:18px}
.brand-name{font-weight:600;line-height:1}
.hero-brand{left:490px;top:38px;color:var(--white);font-size:24px}
.hero-brand .brand-mark{background:var(--white)}
.hero-phone{right:74px;top:52px;color:var(--white);font-size:14px;font-weight:500;display:flex;gap:10px;align-items:center}
.hero-title{left:0;width:1200px;top:290px;text-align:center;color:var(--white);font-size:72px;font-weight:400;letter-spacing:1px}
.hero-sub{left:0;width:1200px;top:382px;text-align:center;color:var(--white);font-family:'Dancing Script',cursive;font-size:36px}
.hero-btn{left:524px;top:452px;width:151px;height:56px;background:var(--orange);color:var(--white);font-size:16px;display:flex;align-items:center;justify-content:center}
.dots{left:1138px;top:322px;display:flex;flex-direction:column;gap:14px}
.dots span{width:13px;height:13px;border-radius:50%;background:var(--white)}
.dots span.on{background:var(--orange)}

/* about */
.eyebrow{position:absolute;font-size:22px;color:var(--ink)}
.big-title{position:absolute;font-size:78px;font-weight:400;line-height:92px}
.accent{color:var(--orange)}

/* services */
.card-title{position:absolute;font-size:36px;color:var(--orange)}

/* featured */
.feature{left:0;top:2524px;width:1200px;height:568px;background:linear-gradient(180deg,#7f9cb8 0%,#a9b7c4 35%,#6d6e70 60%,#4f5752 100%)}
.feature-shade{left:0;top:2524px;width:1200px;height:568px;background:linear-gradient(90deg,rgba(0,0,0,.45),rgba(0,0,0,.05) 60%)}
.tag{left:0;top:2595px;width:207px;height:60px;background:var(--orange);color:var(--white);font-size:27px;font-weight:600;display:flex;align-items:center;justify-content:center}
.feat-copy{left:74px;top:2690px;color:var(--white)}
.feat-copy .label{font-size:19px;font-weight:600}
.feat-copy h2{font-size:48px;font-weight:400;line-height:50px;margin-top:6px}
.feat-copy p{font-size:19px;line-height:29px;margin-top:8px}
.feat-copy .price{font-size:38px;margin-top:10px}
.feat-copy .more{font-size:16px;font-weight:600;text-decoration:underline;margin-top:14px;display:block}
.arrow{top:2780px;width:54px;height:55px;background:#2c2c2c;display:flex;align-items:center;justify-content:center}

/* blog */
.section-center{position:absolute;left:0;width:1200px;text-align:center}
.blog-card{position:absolute;overflow:hidden}
.blog-card .shade{position:absolute;left:0;right:0;bottom:0;height:55%;background:linear-gradient(180deg,rgba(0,0,0,0),rgba(0,0,0,.7))}
.blog-card p{position:absolute;left:26px;bottom:44px;color:var(--white);font-size:28px;line-height:42px}

/* press */
.press{left:0;top:4125px;width:1200px;height:255px;background:var(--light)}
.press-row{left:74px;top:4250px;width:1053px;display:flex;justify-content:space-between;align-items:center}
.press-row span{width:230px;text-align:center;color:#222;font-weight:700;font-size:22px}

/* newsletter & footer */
.news{left:0;top:4380px;width:1200px;height:150px;border-bottom:1px solid var(--line)}
.foot-brand{left:74px;top:4426px;color:var(--orange);font-size:30px}
.foot-brand .brand-mark{background:var(--orange);width:26px;height:26px}
.news-label{left:403px;top:4440px;font-size:20px;font-weight:500}
.news-input{left:650px;top:4428px;width:355px;height:52px;border:1px solid #cfcfcf;font-size:12px;padding-left:18px;display:flex;align-items:center;color:#444}
.news-btn{left:1005px;top:4428px;width:122px;height:52px;background:var(--orange);color:var(--white);font-size:16px;font-weight:600;display:flex;align-items:center;justify-content:center}
.fcol{position:absolute;top:4558px}
.fcol h4{font-size:22px;font-weight:500;margin-bottom:12px}
.fcol li{list-style:none;font-size:14px;line-height:33px;color:var(--ink)}
.social{display:flex;gap:20px;margin-top:14px}
.social span{width:24px;height:24px;border-radius:50%;background:#555}
.rule{left:0;top:4812px;width:1200px;height:1px;background:var(--line)}
.copy{left:0;width:1200px;top:4846px;text-align:center;font-size:13px;color:var(--text)}
</style>
</head>
<body>
<div class="page">

  <!-- Hero -->
  <div class="abs hero" role="img" aria-label="Mediterranean villa with a lit terrace and a curved swimming pool at dusk"></div>
  <div class="abs hero-shade"></div>
  <div class="abs topbar"></div>
  <nav class="abs nav">
    <span class="burger"><span></span><span></span><span></span></span>
    <span>MENU</span><span>OUR PROPERTIES</span><span>ABOUT</span>
  </nav>
  <div class="abs brand hero-brand"><span class="brand-mark"></span><span class="brand-name">CRESTVALE<br>PROPERTIES</span></div>
  <div class="abs hero-phone">
    <svg width="16" height="16" viewBox="0 0 24 24" fill="none" stroke="#fff" stroke-width="2"><path d="M5 3h4l2 5-3 2a11 11 0 0 0 6 6l2-3 5 2v4a2 2 0 0 1-2 2A17 17 0 0 1 3 5a2 2 0 0 1 2-2z"/></svg>
    +188-555-0142
  </div>
  <h1 class="abs hero-title">Crestvale Properties</h1>
  <div class="abs hero-sub">We are a Real Estate company in California</div>
  <div class="abs hero-btn">Learn More</div>
  <div class="abs dots"><span class="on"></span><span></span><span></span><span></span></div>

  <!-- About -->
  <div class="eyebrow" style="left:74px;top:822px">ABOUT</div>
  <h2 class="big-title" style="left:74px;top:848px">Crestvale<br><span class="accent">Properties</span></h2>
  <p class="para" style="left:74px;top:1066px;width:510px">Sed ut perspiciatis unde omnis iste natus error sit voluptatem accusantium doloremque laudantium, totam rem aperiam, eaque ipsa quae ab illo inventore veritatis et quasi architecto beatae vitae dicta sunt explicabo. Nemo enim ipsam voluptatem quia voluptas sit aspernatur aut odit aut fugit, sed quia consequuntur magni dolores eos qui ratione voluptatem sequi nesciunt. Neque porro quisquam est, qui dolorem ipsum quia dolor sit amet, consectetur.</p>
  <div class="btn-outline" style="left:74px;top:1344px;width:152px;height:58px">Learn More</div>
  <div class="abs" style="left:704px;top:824px;width:423px;height:496px;background:var(--orange)"></div>
  <div class="photo" style="left:615px;top:842px;width:495px;height:561px;background:linear-gradient(160deg,#e9e5df,#c9c2b8 55%,#8f8a84)" role="img" aria-label="Smiling real estate agent in a light blazer holding a tablet inside a bright home"></div>

  <!-- Services -->
  <div class="eyebrow" style="right:73px;top:1538px">SERVICES</div>
  <h2 class="big-title" style="right:73px;top:1564px">What <span class="accent">We Do</span></h2>

  <div class="abs" style="left:74px;top:1694px;width:513px;height:226px;background:var(--orange)"></div>
  <div class="photo" style="left:92px;top:1712px;width:478px;height:418px;background:linear-gradient(170deg,#f1f1ef,#d9d7d2 60%,#b9b5ae)" role="img" aria-label="Agent shaking hands with a young couple in a bright empty room"></div>
  <div class="abs" style="left:614px;top:1905px;width:513px;height:225px;background:var(--orange)"></div>
  <div class="photo" style="left:614px;top:1694px;width:494px;height:416px;background:linear-gradient(180deg,#d7e3ea,#9fb08e 40%,#8a5a3e 75%,#b9b9b6)" role="img" aria-label="Modern tropical villa with palm trees, pool and wooden deck"></div>

  <h3 class="card-title" style="left:74px;top:2158px">Property Management</h3>
  <p class="para" style="left:74px;top:2214px;width:510px">Sed ut perspiciatis unde omnis iste natus error sit voluptatem accusantium doloremque laudantium, totam rem aperiam, eaque ipsa quae ab illo inventore veritatis et quasi architecto beatae vitae dicta sunt explicabo. Nemo enim ipsam voluptatem quia voluptas sit aspernatur aut.</p>
  <div class="btn-outline" style="left:74px;top:2398px;width:151px;height:58px">Learn More</div>

  <h3 class="card-title" style="left:614px;top:2158px">Real Estate</h3>
  <p class="para" style="left:614px;top:2214px;width:510px">Sed ut perspiciatis unde omnis iste natus error sit voluptatem accusantium doloremque laudantium, totam rem aperiam, eaque ipsa quae ab illo inventore veritatis et quasi architecto beatae vitae dicta sunt explicabo. Nemo enim ipsam voluptatem quia voluptas sit aspernatur aut.</p>
  <div class="btn-outline" style="left:614px;top:2398px;width:151px;height:58px">Learn More</div>

  <!-- Featured listing -->
  <div class="abs feature" role="img" aria-label="Large modern two-storey house with grey siding and a wide garage at dusk"></div>
  <div class="abs feature-shade"></div>
  <div class="abs tag">For Sale</div>
  <div class="abs feat-copy">
    <div class="label">Featured Listing</div>
    <h2>Excepteur sint occae<br>cat cupidatat</h2>
    <p>Nemo enim ipsam voluptatem<br>quia voluptas sit</p>
    <div class="price">$68,000,000</div>
    <span class="more">Learn More</span>
  </div>
  <div class="abs arrow" style="left:0"><svg width="14" height="20" viewBox="0 0 14 20"><path d="M11 2 3 10l8 8" fill="none" stroke="#fff" stroke-width="2"/></svg></div>
  <div class="abs arrow" style="left:1146px"><svg width="14" height="20" viewBox="0 0 14 20"><path d="m3 2 8 8-8 8" fill="none" stroke="#fff" stroke-width="2"/></svg></div>

  <!-- Blog -->
  <h2 class="section-center" style="top:3136px;font-size:50px;font-weight:400">Blog Post</h2>
  <div class="blog-card" style="left:74px;top:3248px;width:1053px;height:397px;background:linear-gradient(180deg,#e8eef2,#b59a76 45%,#6f8a55 80%)" role="img" aria-label="Modern timber-clad townhouses with balconies and greenery">
    <div class="shade"></div>
    <p>Sed ut perspiciatis unde omnis iste natus<br>error sit voluptatem accusantium</p>
  </div>
  <div class="blog-card" style="left:74px;top:3660px;width:517px;height:397px;background:linear-gradient(160deg,#f2f2f2,#cfcac3 50%,#7d7a76)" role="img" aria-label="Two agents discussing a housing project model at a table">
    <div class="shade"></div>
    <p>Sed ut perspiciatis unde<br>error sit volup</p>
  </div>
  <div class="blog-card" style="left:608px;top:3660px;width:519px;height:397px;background:linear-gradient(170deg,#f4f1ec,#d8cdbd 55%,#8e8477)" role="img" aria-label="Bright open-plan living room with a mezzanine and large windows">
    <div class="shade"></div>
    <p>Sed ut perspiciatis unde<br>error sit volup</p>
  </div>

  <!-- As seen on -->
  <div class="abs press"></div>
  <div class="section-center" style="top:4190px;font-size:24px;font-weight:500">As Seen On</div>
  <div class="abs press-row">
    <span style="font-size:16px">HARBOR LEDGER</span>
    <span>Nookly</span>
    <span style="font-size:18px">Velmora Living</span>
    <span style="font-size:18px">Trevant 9</span>
  </div>

  <!-- Newsletter -->
  <div class="abs news"></div>
  <div class="abs brand foot-brand"><span class="brand-mark"></span><span class="brand-name">CRESTVALE<br>PROPERTIES</span></div>
  <div class="abs news-label">Subscribe Newsletter</div>
  <div class="abs news-input">Email Address</div>
  <div class="abs news-btn">Sign Up</div>

  <!-- Footer -->
  <div class="fcol" style="left:74px"><h4>Site Map</h4><ul><li>Home</li><li>About Us</li><li>Services</li><li>Blog</li><li>Contact Us</li></ul></div>
  <div class="fcol" style="left:323px"><h4>Contact</h4><ul><li>+188-555-0142</li><li>info@crestvalehomes.com</li></ul></div>
  <div class="fcol" style="left:618px"><h4>Address</h4><ul><li style="line-height:28px">Nam libero tempore, cum sol<br>uta nobis est eligendi</li></ul></div>
  <div class="fcol" style="left:925px"><h4>Social Media</h4><div class="social"><span></span><span></span><span></span><span></span><span></span></div></div>
  <div class="abs rule"></div>
  <div class="abs copy">Copyright © 2023, Crestvale Properties All Right reserved</div>
</div>
</body>
</html>
```